Banner Set for a Gay Dating Site

We need animated banners sized 300x250, 300x600, 970x250, 338x235 and 928x244.

Each banner should display 4-6 different men.

Sloagn: "Meet great guys from your area"

A call-to-action-button saying "Register now!"

The logo should be placed on the banner.

Data format: GIF

The banner should be very eye-catching. The banner will be used for the site www.lunamatchbox.net

The banner will be used on sites with lots of videos and there they have to be noticed somehow. And mostly the background on these sites is black.

You can use the attaches images. No stock photos allowed.

Target Market(s)

Men 18-99 yo

Industry/Entity Type

Dating

Requirements
Must have
• Animated Subjects
Should not have
• Rainbows

```html
<!DOCTYPE html>
<html lang="en">
<head>
<meta charset="utf-8">
<title>Luna Matchbox – Banner Set</title>
<link href="https://fonts.googleapis.com/css2?family=Roboto+Condensed:wght@400;700&display=swap" rel="stylesheet">
<style>
  :root{
    --board:#414141;
    --gold:#a38540;
    --black:#000;
    --white:#fff;
    --panel:rgba(0,0,0,.78);
    --skin-warm:#d9b08f;
    --skin-light:#e6cdb8;
    --skin-pale:#dcd6d2;
    --foliage:#4f6a3a;
    --wall-cream:#efd9b4;
    --shadow-grey:#3a3a3a;
  }
  *{margin:0;padding:0;box-sizing:border-box}
  html,body{width:1200px;height:955px;overflow:hidden;background:var(--board)}
  body{position:relative;font-family:"Roboto Condensed",Arial,sans-serif;color:var(--white)}

  .accent-shape{position:absolute;left:0;top:0}
  .size-label{position:absolute;font-weight:700;font-size:19px;letter-spacing:.2px}
  .banner{position:absolute;background:var(--black);overflow:hidden}
  .banner svg{position:absolute;left:0;top:0;display:block}

  .photo{position:absolute}
  .tone-warm{background:linear-gradient(160deg,var(--wall-cream),var(--skin-warm))}
  .tone-light{background:linear-gradient(160deg,#f1efec,var(--skin-light))}
  .tone-pale{background:linear-gradient(160deg,#e9e7e4,var(--skin-pale))}
  .tone-green{background:linear-gradient(160deg,var(--foliage),var(--skin-warm))}

  .pitch{position:absolute;text-align:center;display:flex;flex-direction:column;align-items:center}
  .brand{color:var(--gold);font-weight:700;text-transform:uppercase;letter-spacing:1px;line-height:1}
  .slogan{font-weight:700;line-height:1.2}
  .cta{background:var(--gold);color:var(--white);font-weight:700;border-radius:20px;display:flex;align-items:center;justify-content:center}

  /* 300x250 */
  .b-300x250{left:80px;top:120px;width:240px;height:200px;background:var(--board)}
  .b-300x250 .overlay{position:absolute;left:32px;top:53px;width:176px;height:147px;background:var(--panel)}
  .b-300x250 .pitch{left:32px;top:72px;width:176px}
  .b-300x250 .brand{font-size:15px;margin-bottom:22px}
  .b-300x250 .slogan{font-size:14px}
  .b-300x250 .cta{width:88px;height:24px;font-size:9px;margin-top:10px}

  /* 970x250 */
  .b-970x250{left:345px;top:120px;width:776px;height:200px}
  .b-970x250 .pitch{left:410px;top:38px;width:200px}
  .b-970x250 .brand{font-size:22px;margin-bottom:32px}
  .b-970x250 .slogan{font-size:17px}
  .b-970x250 .cta{width:102px;height:29px;font-size:11px;margin-top:15px}

  /* 300x600 */
  .b-300x600{left:80px;top:398px;width:240px;height:480px;background:var(--black)}
  .b-300x600 .pitch{left:0;top:330px;width:240px}
  .b-300x600 .brand{font-size:22px;margin-bottom:26px}
  .b-300x600 .slogan{font-size:17px}
  .b-300x600 .cta{width:101px;height:30px;font-size:11px;margin-top:15px}

  /* 338x235 */
  .b-338x235{left:345px;top:398px;width:270px;height:188px}
  .b-338x235 .pitch{left:120px;top:74px;width:150px}
  .b-338x235 .brand{font-size:16px;margin-bottom:24px}
  .b-338x235 .slogan{font-size:13.5px}
  .b-338x235 .cta{width:78px;height:22px;font-size:8px;margin-top:12px}

  /* 928x244 */
  .b-928x244{left:345px;top:683px;width:742px;height:195px}
  .b-928x244 .pitch{left:555px;top:38px;width:180px}
  .b-928x244 .brand{font-size:22px;margin-bottom:29px}
  .b-928x244 .slogan{font-size:17px}
  .b-928x244 .cta{width:99px;height:29px;font-size:11px;margin-top:15px}
</style>
</head>
<body>

<svg class="accent-shape" width="1200" height="955" viewBox="0 0 1200 955" aria-hidden="true">
  <polygon points="1030,0 1200,0 1200,740 928,502" fill="var(--gold)"/>
</svg>

<div class="size-label" style="left:79px;top:72px">300x250</div>
<div class="size-label" style="left:344px;top:72px">970x250</div>
<div class="size-label" style="left:79px;top:353px">300x600</div>
<div class="size-label" style="left:344px;top:353px">338x235</div>
<div class="size-label" style="left:344px;top:635px">928x244</div>

<!-- 300x250 -->
<section class="banner b-300x250">
  <div class="photo tone-warm" style="left:0;top:0;width:119px;height:98px" role="img" aria-label="Photo of a man in a harness"></div>
  <div class="photo tone-light" style="left:121px;top:0;width:119px;height:98px" role="img" aria-label="Photo of a young shirtless man"></div>
  <div class="photo tone-pale" style="left:0;top:100px;width:119px;height:100px" role="img" aria-label="Photo of a shirtless man"></div>
  <div class="photo tone-warm" style="left:121px;top:100px;width:119px;height:100px" role="img" aria-label="Photo of a smiling young man"></div>
  <div class="overlay"></div>
  <div class="pitch">
    <div class="brand">Luna Matchbox</div>
    <div class="slogan">Meet great guys from<br>your area</div>
    <div class="cta">Register now!</div>
  </div>
</section>

<!-- 970x250 -->
<section class="banner b-970x250">
  <svg width="776" height="200" viewBox="0 0 776 200">
    <rect width="776" height="200" fill="var(--black)"/>
    <polygon points="0,0 32,0 210,80 165,200 0,200" fill="var(--skin-warm)" role="img" aria-label="Photo of a bearded man in an open shirt"/>
    <polygon points="36,0 248,0 212,74" fill="var(--shadow-grey)" role="img" aria-label="Dark photo of a man"/>
    <polygon points="254,0 420,0 362,140 218,80" fill="var(--foliage)" role="img" aria-label="Photo of a blond man outdoors"/>
    <polygon points="216,86 358,146 336,200 170,200" fill="var(--skin-light)" role="img" aria-label="Photo of a smiling young man"/>
    <polygon points="682,0 776,0 776,200 596,200" fill="var(--skin-pale)" role="img" aria-label="Photo of a man in a tank top"/>
  </svg>
  <div class="pitch">
    <div class="brand">Luna Matchbox</div>
    <div class="slogan">Meet great guys from<br>your area</div>
    <div class="cta">Register now!</div>
  </div>
</section>

<!-- 300x600 -->
<section class="banner b-300x600">
  <div class="photo tone-warm" style="left:0;top:0;width:118px;height:98px" role="img" aria-label="Photo of a man in a harness"></div>
  <div class="photo tone-light" style="left:122px;top:0;width:118px;height:98px" role="img" aria-label="Photo of a young shirtless man"></div>
  <div class="photo tone-light" style="left:0;top:102px;width:118px;height:98px" role="img" aria-label="Photo of a man in red shorts"></div>
  <div class="photo tone-pale" style="left:122px;top:102px;width:118px;height:98px" role="img" aria-label="Photo of a young man in a harness"></div>
  <div class="photo tone-warm" style="left:0;top:204px;width:118px;height:98px" role="img" aria-label="Photo of a bearded man in an open shirt"></div>
  <div class="photo tone-green" style="left:122px;top:204px;width:118px;height:98px" role="img" aria-label="Photo of a smiling young man"></div>
  <div class="pitch">
    <div class="brand">Luna Matchbox</div>
    <div class="slogan">Meet great guys from<br>your area</div>
    <div class="cta">Register now!</div>
  </div>
</section>

<!-- 338x235 -->
<section class="banner b-338x235">
  <svg width="270" height="188" viewBox="0 0 270 188">
    <rect width="270" height="188" fill="var(--black)"/>
    <polygon points="0,0 160,0 122,128 0,94" fill="var(--foliage)" role="img" aria-label="Photo of a blond man outdoors"/>
    <polygon points="0,99 120,134 86,188 0,188" fill="var(--skin-light)" role="img" aria-label="Photo of a smiling young man"/>
    <polygon points="165,0 270,0 270,78 152,30" fill="var(--skin-warm)" role="img" aria-label="Photo of a smiling dark-haired man"/>
  </svg>
  <div class="pitch">
    <div class="brand">Luna Matchbox</div>
    <div class="slogan">Meet great guys from<br>your area</div>
    <div class="cta">Register now!</div>
  </div>
</section>

<!-- 928x244 -->
<section class="banner b-928x244">
  <svg width="742" height="195" viewBox="0 0 742 195">
    <g fill="var(--skin-light)">
      <polygon transform="translate(66,71)" points="-54,0 -27,-47 27,-47 54,0 27,47 -27,47" role="img" aria-label="Photo of a young shirtless man"/>
      <polygon transform="translate(154,122)" points="-54,0 -27,-47 27,-47 54,0 27,47 -27,47" fill="var(--skin-pale)" role="img" aria-label="Photo of a young man in a harness"/>
      <polygon transform="translate(239,71)" points="-54,0 -27,-47 27,-47 54,0 27,47 -27,47" fill="var(--skin-pale)" role="img" aria-label="Photo of a man in a tank top"/>
      <polygon transform="translate(326,122)" points="-54,0 -27,-47 27,-47 54,0 27,47 -27,47" fill="var(--skin-warm)" role="img" aria-label="Photo of a man in a harness"/>
      <polygon transform="translate(411,71)" points="-54,0 -27,-47 27,-47 54,0 27,47 -27,47" fill="var(--foliage)" role="img" aria-label="Photo of a blond man outdoors"/>
      <polygon transform="translate(498,122)" points="-54,0 -27,-47 27,-47 54,0 27,47 -27,47" role="img" aria-label="Photo of a man in red shorts"/>
    </g>
  </svg>
  <div class="pitch">
    <div class="brand">Luna Matchbox</div>
    <div class="slogan">Meet great guys from<br>your area</div>
    <div class="cta">Register now!</div>
  </div>
</section>

</body>
</html>
```